Stylish Business Cards Wanted

- DOUBLE SIDED Design Required -

High end, edgy cards for a corporate and personal stylist. Must include logo,
Name: Belinda Forsey
Title: Director and Stylist
telephone : +61 8 8217 4592
email: belinda@thegarbledger.example
website: thegarbledger.example
Tag: Corporate Workwear & Uniform Specialist | Personal Stylist
Would like nice icons for telephone, email, website

Target Market(s)

Businesses wanting stylish uniforms, people wanting stylish wardrobes

Industry/Entity Type

Corporate Workwear Stylist

Contact Information for Business Card

I would like black, white and gold foiling incorporated in the design - possibly a touch of the other colours on my branding guide attached Name: Belinda Forsey Title: Director and Stylist telephone : +61 8 8217 4592 email: belinda@thegarbledger.example website: thegarbledger.example Tag: Corporate Workwear & Uniform Specialist | Personal Stylist Would like nice icons for telephone, email, website

Font styles to use
Other font styles liked:
• Raleway

Colors

Designer to choose colors to be used in the design.

Requirements
Must have
• Gold foil accents

```html
<!DOCTYPE html>
<html lang="en">
<head>
<meta charset="utf-8">
<title>The Garb Ledger – Business Cards</title>
<link rel="stylesheet" href="https://fonts.googleapis.com/css2?family=Great+Vibes&family=Raleway:wght@500;700&family=Arimo:wght@400&display=swap">
<style>
  :root {
    --page: #e9e8e6;
    --card: #262627;
    --card-deep: #1c1c1d;
    --gold: #e0b84c;
    --white: #ffffff;
    --soft-white: #e6e6e6;
    --rule: #bdbdbd;
  }
  * { box-sizing: border-box; margin: 0; padding: 0; }
  html, body { width: 1200px; height: 801px; overflow: hidden; }
  body {
    background: var(--page);
    display: flex;
    align-items: center;
    justify-content: center;
    gap: 40px;
  }
  .card {
    width: 540px;
    height: 330px;
    background: var(--card);
    position: relative;
    overflow: hidden;
  }

  /* Contact side */
  .card--contact { display: flex; align-items: center; }
  .brand-block {
    width: 220px;
    display: flex;
    justify-content: center;
  }
  .brand-name {
    font-family: "Raleway", sans-serif;
    font-weight: 700;
    color: var(--white);
    font-size: 26px;
    line-height: 1.15;
    text-align: center;
    letter-spacing: 1px;
  }
  .divider {
    width: 1px;
    height: 120px;
    background: var(--rule);
  }
  .contact-block {
    padding-left: 30px;
    color: var(--soft-white);
    font-family: "Arimo", sans-serif;
  }
  .person-name {
    font-family: "Great Vibes", cursive;
    color: var(--gold);
    font-size: 36px;
    line-height: 1;
  }
  .person-title { font-size: 14px; margin: 4px 0 16px; }
  .contact-list { list-style: none; font-size: 13px; }
  .contact-list li {
    display: flex;
    align-items: center;
    gap: 8px;
    margin-bottom: 5px;
  }
  .contact-list svg { width: 12px; height: 12px; flex: none; }
  .accent { color: var(--gold); }

  /* Brand side */
  .card--brand {
    display: flex;
    flex-direction: column;
    align-items: center;
    justify-content: center;
  }
  .pattern-field {
    position: absolute;
    inset: 0;
    background: radial-gradient(ellipse at center, #2a2a2b 0%, var(--card-deep) 100%);
  }
  .brand-name--gold {
    position: relative;
    color: var(--gold);
    font-size: 44px;
    margin-top: -20px;
  }
  .tagline {
    position: absolute;
    left: 0; right: 0; bottom: 30px;
    text-align: center;
    font-family: "Arimo", sans-serif;
    font-weight: 400;
    color: var(--gold);
    font-size: 12.5px;
    letter-spacing: 0.5px;
    text-transform: uppercase;
  }
</style>
</head>
<body>

  <section class="card card--contact" aria-label="Contact side">
    <div class="brand-block">
      <p class="brand-name">The Garb<br>Ledger</p>
    </div>
    <div class="divider"></div>
    <div class="contact-block">
      <p class="person-name">Belinda Forsey</p>
      <p class="person-title">Director and Stylist</p>
      <ul class="contact-list">
        <li>
          <svg viewBox="0 0 12 12" aria-hidden="true"><circle cx="6" cy="6" r="6" fill="var(--gold)"/><path d="M4 3.2c.4-.3.8 0 1 .5l.3.7c.1.3 0 .5-.2.7l-.3.2c.3.8.9 1.4 1.7 1.8l.3-.3c.2-.2.4-.2.7-.1l.7.3c.5.2.7.6.4 1-.4.6-1 .8-1.7.5C5.2 7.8 4.3 6.9 3.7 5.2c-.3-.8 0-1.5.3-2z" fill="var(--card)"/></svg>
          +61 8 8217 4592
        </li>
        <li>
          <svg viewBox="0 0 12 12" aria-hidden="true"><rect x="0.5" y="2.5" width="11" height="7.5" rx="1" fill="var(--gold)"/><path d="M1 3l5 3.8L11 3" fill="none" stroke="var(--card)" stroke-width="1"/></svg>
          belinda@thegarbledger.example
        </li>
        <li>
          <svg viewBox="0 0 12 12" aria-hidden="true"><circle cx="6" cy="6" r="5.5" fill="var(--gold)"/><path d="M0.8 6h10.4M6 0.8c-2.2 2.8-2.2 7.6 0 10.4M6 0.8c2.2 2.8 2.2 7.6 0 10.4" fill="none" stroke="var(--card)" stroke-width="0.8"/></svg>
          <span>www.<span class="accent">thegarbledger</span>.example</span>
        </li>
      </ul>
    </div>
  </section>

  <section class="card card--brand" aria-label="Brand side">
    <div class="pattern-field" role="img" aria-label="Embossed black damask scroll pattern across the card"></div>
    <p class="brand-name brand-name--gold">The Garb Ledger</p>
    <p class="tagline">Corporate Workwear | Uniform Specialist | Personal Stylist</p>
  </section>

</body>
</html>
```